Back Pain

Need a flyer similar to the attached draft. This is to be handed out to prospective patients. Note that Sketch Hive has already designed the logo. If you need a copy please contact me

```html
<!DOCTYPE html>
<html lang="en">
<head>
<meta charset="UTF-8">
<title>Spine Ease Clinic – Tech Neck Flyer</title>
<link href="https://fonts.googleapis.com/css2?family=Montserrat:wght@500;600;700;800&display=swap" rel="stylesheet">
<style>
  :root{
    --stage:#a9a9a9;
    --paper:#ffffff;
    --blue:#1b74c8;
    --sky:#3d9fe3;
    --green:#8cc63f;
    --leaf:#5cbf6c;
    --ink:#1f2a36;
    --band:#2e3944;
  }
  *{box-sizing:border-box;margin:0;padding:0}
  html,body{width:1200px;height:1200px;overflow:hidden;background:var(--stage)}
  body{font-family:"Montserrat",Arial,sans-serif;position:relative}
  .flyer{position:absolute;left:192px;top:72px;width:811px;height:1050px;background:var(--paper);overflow:hidden;box-shadow:0 6px 18px rgba(0,0,0,.25)}
  .shapes{position:absolute;left:0;top:0}
  .abs{position:absolute}
  .brand{left:0;width:420px;top:28px;text-align:center}
  .brand-mark{display:block;margin:0 auto 6px}
  .brand-name{font-weight:700;font-size:19px;line-height:20px;color:var(--blue);letter-spacing:-.2px}
  .brand-sub{font-weight:700;font-size:9.5px;line-height:11px;color:var(--blue);letter-spacing:1px;margin-top:1px}
  .stat{left:21px;top:226px;color:#fff;font-weight:600;font-size:22.5px;line-height:1.25}
  .stat strong{display:block;font-size:32px;font-weight:700;line-height:1.05}
  .stat .stat-tail{letter-spacing:.9px}
  .chart-note{left:40px;top:447px;font-size:20px;font-weight:500;color:var(--ink);line-height:1.23}
  .bar-val,.bar-deg{position:absolute;width:32px;text-align:center;font-size:16px;color:#fff;font-weight:500}
  .axis-x{left:46px;top:650px;font-size:14.5px;font-weight:600;color:var(--ink)}
  .axis-y{left:314px;top:618px;transform:rotate(-90deg);transform-origin:0 0;font-size:13px;font-weight:600;color:var(--ink);line-height:1.1;width:120px}
  .checklist{left:546px;top:449px;list-style:none}
  .checklist li{display:flex;align-items:center;height:32px;color:#fff;font-weight:700;font-size:23.5px}
  .checklist svg{margin-right:10px;flex:none}
  .help-title{left:68px;top:700px;width:682px;height:58px;line-height:58px;text-align:center;color:#fff;font-weight:700;font-size:34px;letter-spacing:.3px}
  .help-text{left:46px;top:771px;width:725px;text-align:center;color:#fff;font-weight:700;font-size:20px;line-height:1.2}
  .doc-name{left:210px;top:882px;font-weight:800;font-size:22px;color:#fff}
  .doc-name span{color:var(--green)}
  .doc-info{left:180px;top:910px;font-weight:600;font-size:16.5px;color:#fff;display:flex;align-items:center;gap:6px}
  .off{left:18px;top:930px;color:#fff;font-weight:800;font-size:54px;line-height:.95}
  .offer{left:210px;top:958px;font-weight:700;font-size:17.5px;color:var(--ink);line-height:1.1}
  .offer span{color:var(--green)}
  .web{left:445px;top:1018px;color:#fff;font-weight:700;font-size:17px;display:flex;align-items:center;gap:10px}
</style>
</head>
<body>
<div class="flyer">
  <svg class="shapes" width="811" height="1050" viewBox="0 0 811 1050">
    <defs>
      <linearGradient id="swoosh" x1="0" y1="0" x2="1" y2="0.4">
        <stop offset="0" stop-color="#3aa3df"/>
        <stop offset="1" stop-color="#66c777"/>
      </linearGradient>
      <linearGradient id="photoFill" x1="0" y1="0" x2="1" y2="1">
        <stop offset="0" stop-color="#2b3d55"/>
        <stop offset=".55" stop-color="#a7b4c2"/>
        <stop offset="1" stop-color="#e8ecef"/>
      </linearGradient>
    </defs>
    <path d="M0 170 C120 150 260 158 400 190 L400 378 C260 372 120 395 0 420 Z" fill="var(--leaf)"/>
    <path d="M0 180 C120 162 260 170 400 200 L400 368 C260 362 120 385 0 410 Z" fill="url(#swoosh)"/>
    <circle cx="614" cy="415" r="258" fill="var(--sky)"/>
    <circle cx="608" cy="212" r="222" fill="#fff"/>
    <circle cx="608" cy="212" r="212" fill="url(#photoFill)" role="img" aria-label="Photo: office worker holding his sore neck while looking at a smartphone"/>
    <rect y="0" width="811" height="16" fill="var(--blue)"/>
    <g fill="var(--green)">
      <rect x="46" y="583" width="32" height="33"/>
      <rect x="101" y="560" width="32" height="56"/>
      <rect x="158" y="535" width="32" height="81"/>
      <rect x="220" y="512" width="32" height="104"/>
      <rect x="278" y="489" width="32" height="127"/>
    </g>
    <g fill="var(--blue)">
      <rect x="46" y="616" width="32" height="25"/>
      <rect x="101" y="616" width="32" height="25"/>
      <rect x="158" y="616" width="32" height="25"/>
      <rect x="220" y="616" width="32" height="25"/>
      <rect x="278" y="616" width="32" height="25"/>
    </g>
    <rect x="46" y="728" width="725" height="105" fill="var(--blue)"/>
    <path d="M393 833 L423 833 L408 849 Z" fill="var(--blue)"/>
    <rect x="64" y="696" width="690" height="66" rx="33" fill="#fff"/>
    <rect x="68" y="700" width="682" height="58" rx="29" fill="var(--green)"/>
    <rect y="868" width="811" height="78" fill="var(--band)"/>
    <path d="M415 1050 L415 1030 Q415 1008 437 1008 L811 1008 L811 1050 Z" fill="var(--blue)"/>
    <circle cx="3" cy="1043" r="180" fill="#fff"/>
    <circle cx="3" cy="1043" r="170" fill="var(--sky)"/>
  </svg>

  <div class="abs brand">
    <svg class="brand-mark" width="78" height="78" viewBox="0 0 78 78"><circle cx="39" cy="39" r="36" fill="var(--blue)"/></svg>
    <div class="brand-name">SPINE EASE CLINIC</div>
    <div class="brand-sub">DR BEN HARPER - CHIROPRACTOR</div>
  </div>

  <div class="abs stat">The average person spends<strong>8-11 hours per day</strong><span class="stat-tail">using electronic devices.</span></div>

  <div class="abs chart-note">As the head tilts forward,<br>more force is placed<br>on the spine.</div>
  <div class="bar-val" style="left:46px;top:592px">12</div>
  <div class="bar-val" style="left:101px;top:592px">27</div>
  <div class="bar-val" style="left:158px;top:592px">40</div>
  <div class="bar-val" style="left:220px;top:592px">49</div>
  <div class="bar-val" style="left:278px;top:592px">60</div>
  <div class="bar-deg" style="left:46px;top:618px">0°</div>
  <div class="bar-deg" style="left:101px;top:618px">15°</div>
  <div class="bar-deg" style="left:158px;top:618px">30°</div>
  <div class="bar-deg" style="left:220px;top:618px">45°</div>
  <div class="bar-deg" style="left:278px;top:618px">60°</div>
  <div class="abs axis-x">DEGREES OF FORWARD HEAD TILT</div>
  <div class="abs axis-y">PRESURE<br>ON SPINE (LBS)</div>

  <ul class="abs checklist">
    <li><svg width="22" height="22" viewBox="0 0 22 22"><circle cx="11" cy="11" r="9" fill="none" stroke="#fff" stroke-width="2"/><path d="M6 11 l4 4 l9 -10" fill="none" stroke="#fff" stroke-width="2.2"/></svg>Headaches</li>
    <li><svg width="22" height="22" viewBox="0 0 22 22"><circle cx="11" cy="11" r="9" fill="none" stroke="#fff" stroke-width="2"/><path d="M6 11 l4 4 l9 -10" fill="none" stroke="#fff" stroke-width="2.2"/></svg>Neck Pain</li>
    <li><svg width="22" height="22" viewBox="0 0 22 22"><circle cx="11" cy="11" r="9" fill="none" stroke="#fff" stroke-width="2"/><path d="M6 11 l4 4 l9 -10" fill="none" stroke="#fff" stroke-width="2.2"/></svg>Shoulder Pain</li>
    <li><svg width="22" height="22" viewBox="0 0 22 22"><circle cx="11" cy="11" r="9" fill="none" stroke="#fff" stroke-width="2"/><path d="M6 11 l4 4 l9 -10" fill="none" stroke="#fff" stroke-width="2.2"/></svg>Back Pain</li>
    <li><svg width="22" height="22" viewBox="0 0 22 22"><circle cx="11" cy="11" r="9" fill="none" stroke="#fff" stroke-width="2"/><path d="M6 11 l4 4 l9 -10" fill="none" stroke="#fff" stroke-width="2.2"/></svg>Hand &amp; Arm Pain</li>
    <li><svg width="22" height="22" viewBox="0 0 22 22"><circle cx="11" cy="11" r="9" fill="none" stroke="#fff" stroke-width="2"/><path d="M6 11 l4 4 l9 -10" fill="none" stroke="#fff" stroke-width="2.2"/></svg>Sciatica</li>
  </ul>

  <div class="abs help-title">CHIROPRACTIC CARE CAN HELP</div>
  <div class="abs help-text">CORRECT AND PREVENT THESE PROBLEMS BY RESTORING<br>AND MAINTAINING PROPER ALIGNMENT OF THE NECK</div>

  <div class="abs doc-name"><span>DR. BENJAMIN HARPER</span> - CHIROPRACTOR</div>
  <div class="abs doc-info">
    <svg width="12" height="16" viewBox="0 0 12 16"><path d="M6 0 C2.7 0 0 2.6 0 5.8 C0 10 6 16 6 16 C6 16 12 10 12 5.8 C12 2.6 9.3 0 6 0 Z" fill="var(--sky)"/><circle cx="6" cy="6" r="2.2" fill="var(--band)"/></svg>
    NORTHGATE AT 42 HARBOUR RD. CORNER SUITE
    <svg width="18" height="18" viewBox="0 0 18 18" style="margin-left:10px"><path d="M4 2 L7 2 L8 6 L6 7.5 C7 10 8.5 11.5 10.5 12.5 L12 10.5 L16 11.5 L16 14.5 C16 15.5 15 16 14 16 C8 15.5 2.5 10 2 4 C2 3 3 2 4 2 Z" fill="var(--sky)"/></svg>
    0400 555 019
  </div>

  <div class="abs off">50%<br>OFF</div>
  <div class="abs offer">50% OFF INITIAL CONSULTATION IF NOW BOOK ONLINE<br>AT OUR WEBSITE AND CHOOSE “<span>TECHNECK</span>” OPTION</div>
  <div class="abs web">
    <svg width="20" height="20" viewBox="0 0 20 20" fill="none" stroke="#fff" stroke-width="1.6"><circle cx="10" cy="10" r="8.5"/><ellipse cx="10" cy="10" rx="3.8" ry="8.5"/><path d="M1.5 10 H18.5 M3 5.5 H17 M3 14.5 H17"/></svg>
    WWW.SPINEEASECLINIC.EXAMPLE
  </div>
</div>
</body>
</html>
```